依頼詳細
店舗名はゆるりテラスといいます(www.yururi-terasu.com)
和モダンスタイルのリラクゼーションサロンです。
今回は西宮店の外装リニューアルになります。
ホームページにあるようにもともとは木枠に杉板を垂直に取り付けた外観だったのですが一部が崩れてしまい現在は半分以上撤去しております(写真参照)
今回の外装工事にあたって一度すべて撤去してやり替える予定です。
メインの外装材はミナト塗研のベルナスコート(https://www.minato-token.co.jp/nfd/products/bernascoat/)を予定しておりますので、この中から部材を選定いただき、和モダンスタイルのデザインでお願いします。
屋根付近の水色の雨どいは塗装するので何色でも可能です。
また、店舗入り口上部に雨除けテントも設置可能なのでそれをとりつけたイメージもお願いします。
10年前の工事の際に店舗敷地周囲の地面にコンクリートで型枠を作っていたのですが、今回のリニューアルでその部分が露出してしまい汚らしくなるのでその部分はタイル施工や小さなウッドテラスで隠そうかと考えておりますのでその部分も合わせたデザインでお願いします。

看板は西側上部(店舗入り口側)と、南側上部(駐車場側)と北西側(斜め)の3つと
店舗入り口両サイドに2つの計5つです。

・西側上部と南側上部の看板
こちらの看板は店舗のメイン看板になり、多少サイズは異なりますがどちらも同じデザインで問題ありません。
看板の記載内容など多少かわりますが、とりあえず現状と同じ内容で作成お願いします。
現状は和を意識した深緑色ですが、いっそのことガラッとイメージをかえたいので別の色でも問題ありません。特に希望はありません。

・北西側看板
こちらの看板はイメージ看板や店舗のアピール看板などおまかせでお願いします。
メインの看板仕様は外装材の上に直接取り付けるパネル看板ですが、それプラス、ロゴマークなどを利用した立体ロゴ看板などおしゃれな感じであればなんでもかまいません。

・店舗入り口看板
向かって右側にメニュー看板をお願いします。
デザインはおまかせします。
向かって左側は店舗アピール看板でお願いします。
こちらも立体ロゴ文字など特に希望はないのでおまかせでお願いします。

全体的なイメージは和モダンスタイルのおしゃれなイメージです。
チェーン店のような安心感のあるデザインがいいです。

大手さんだとQuiloなどがイメージに近いです。
記載項目
店名:ゆるりテラス西宮店 URL:www.yururi-terasu.com
大きな幹線道路(171号線)沿いの角地にあるとてもよく目立つ店舗です。

看板サイズ
西側上部看板:W7,200×H1,500
南側上部看板:W6450×H1,500
北西看板:サイズ指定なし
店舗入り口メニュー看板:W1,800×W1,800 ※パネル看板
店舗入り口アピール看板:サイズ指定なし

店舗壁面サイズ
北西面:W9,200×H3,520
西面:W6,800×H2,600 (自動ドアサイズ:W1,800×H2,400)
南面:W6,800×H2,600 (シャッターサイズW1,800×H1,400)
希望イメージ
シンプル 複雑
単色 カラフル
暗い 明るい
日常 高級
遊び心 厳粛
未来的 伝統的
女性的 男性的
希望する色
納品ファイル
• イラストレーター形式 (.ai)
• フォトショップ形式 (.psd)
補足説明
ロゴデータ、現状の写真を添付します。
ロゴデータを添付いたしました。
よろしくお願いします。
■ 選んだ理由

ぱっと見の雰囲気やデザイン、クオリティーも高く気に入りました。

■ 提案者全員のお礼・コメント

たくさんのご提案ありがとうございました。

```html
<!DOCTYPE html>
<html lang="ja">
<head>
<meta charset="utf-8">
<title>ゆるりテラス 外装立面</title>
<link href="https://fonts.googleapis.com/css2?family=M+PLUS+Rounded+1c:wght@500;700&family=Noto+Sans+JP:wght@400;700&display=swap" rel="stylesheet">
<style>
:root{
  --bg:#ffffff;
  --wood-light:#e9cf9e;
  --wood-mid:#dcb980;
  --wood-dark:#c99f62;
  --parapet:#2a2420;
  --ink:#2b2b2b;
  --leaf:#8cc63f;
  --leaf-dark:#5f9b1f;
  --sign:#ffffff;
  --note:#555;
  --glass:#3b3b3b;
  --shutter:#f4f4f4;
}
*{margin:0;padding:0;box-sizing:border-box}
html,body{width:1200px;height:341px;overflow:hidden;background:var(--bg)}
body{position:relative;font-family:"Noto Sans JP",sans-serif;color:var(--ink)}
.abs{position:absolute}
.wall{background:repeating-linear-gradient(90deg,var(--wood-light) 0 14px,var(--wood-mid) 14px 15px,var(--wood-light) 15px 38px,var(--wood-dark) 38px 39px);border-top:3px solid var(--parapet)}
.note{font-size:6px;color:var(--note);white-space:nowrap}
.brand{font-family:"M PLUS Rounded 1c",sans-serif;font-weight:700;color:var(--ink);white-space:nowrap;line-height:1}
.brand-sub{font-family:"Noto Sans JP",sans-serif;font-weight:700;letter-spacing:.12em;white-space:nowrap;line-height:1}
.dot{border-radius:50%;background:var(--ink)}
.sign{background:var(--sign);border:1px solid #ccc;overflow:hidden}
.tagline{font-weight:700;white-space:nowrap;line-height:1;letter-spacing:-.02em}
.photo{background:linear-gradient(90deg,rgba(255,255,255,1),#f3e1d2 35%,#d8b8a0)}
.door{background:#fff;border:2px solid #222;display:flex;gap:4px;padding:6px 5px 3px}
.door span{flex:1;background:var(--glass)}
.poster{background:linear-gradient(#f7f4ee,#e9e2d6);border:1px solid #999}
.menu{background:#fff;border:1px solid #999;padding:3px 4px;display:flex;flex-direction:column;gap:3px}
.menu-head{background:var(--leaf);color:#fff;font-size:5px;font-weight:700;padding:1px 3px;white-space:nowrap}
.menu-row{font-size:4px;line-height:1.4;color:#333;white-space:nowrap}
.shutter{background:repeating-linear-gradient(var(--shutter) 0 3px,#ccc 3px 4px);border:2px solid #888}
</style>
</head>
<body>
<div class="abs note" style="left:130px;top:63px">カルプ切り文字:W5,300×H1,300</div>
<div class="abs wall" style="left:22px;top:70px;width:456px;height:195px"></div>
<div class="abs dot" style="left:124px;top:108px;width:34px;height:34px"></div>
<div class="abs brand" style="left:168px;top:104px;font-size:38px">ゆるりテラス</div>
<div class="abs brand-sub" style="left:214px;top:160px;font-size:12px">YURURI TERASU</div>
<div class="abs note" style="left:22px;top:282px">壁面:木目調仕上げ-58-B</div>
<div class="abs note" style="left:22px;top:291px">パラペット=笠木:黒塗装</div>

<div class="abs note" style="left:478px;top:50px">西側上部看板:W7,200×H1,500</div>
<div class="abs note" style="left:840px;top:50px">南側上部看板:W6450×H1,500</div>
<div class="abs wall" style="left:476px;top:138px;width:688px;height:140px;border-top:none"></div>

<div class="abs sign" style="left:478px;top:60px;width:362px;height:78px">
  <div class="abs photo" role="img" aria-label="施術を受けてくつろぐ女性の写真" style="left:200px;top:0;width:162px;height:78px"></div>
  <div class="abs tagline" style="left:10px;top:9px;font-size:9px">ココロに、カラダに、心地いい。15分850円からの極上リラクゼーション!</div>
  <div class="abs dot" style="left:26px;top:34px;width:20px;height:20px;background:var(--leaf)"></div>
  <div class="abs brand" style="left:52px;top:31px;font-size:24px">ゆるりテラス</div>
  <div class="abs brand-sub" style="left:90px;top:62px;font-size:7px;color:var(--leaf-dark)">YURURI TERASU</div>
</div>
<div class="abs sign" style="left:840px;top:60px;width:324px;height:78px">
  <div class="abs photo" role="img" aria-label="脚のマッサージを受ける様子の写真" style="left:180px;top:0;width:144px;height:78px"></div>
  <div class="abs tagline" style="left:8px;top:9px;font-size:8.4px">ココロに、カラダに、心地いい。15分850円からの極上リラクゼーション!</div>
  <div class="abs dot" style="left:26px;top:34px;width:20px;height:20px;background:var(--leaf)"></div>
  <div class="abs brand" style="left:52px;top:31px;font-size:24px">ゆるりテラス</div>
  <div class="abs brand-sub" style="left:90px;top:62px;font-size:7px;color:var(--leaf-dark)">YURURI TERASU</div>
</div>

<div class="abs poster" role="img" aria-label="店内施術風景の写真とロゴを配したアピール看板" style="left:518px;top:154px;width:36px;height:98px"></div>
<div class="abs door" style="left:576px;top:180px;width:72px;height:96px"><span></span><span></span></div>
<div class="abs menu" style="left:658px;top:154px;width:92px;height:98px">
  <div class="menu-head">ボディケア 10分毎 1,000円</div>
  <div class="menu-row">30分 3,000円　60分 5,800円<br>90分 8,500円　120分 11,000円</div>
  <div class="menu-head">フットケア 10分毎 1,000円</div>
  <div class="menu-row">30分 3,000円　60分 5,800円</div>
  <div class="menu-head">アロマ 10分毎 1,500円</div>
  <div class="menu-row">60分 7,800円　90分 11,000円</div>
</div>
<div class="abs shutter" style="left:894px;top:174px;width:78px;height:76px"></div>

<div class="abs note" style="left:498px;top:284px">店舗入り口アピール看板:W900×H1,800</div>
<div class="abs note" style="left:658px;top:284px">店舗入り口メニュー看板:W1,800×H1,800</div>
</body>
</html>
```